Thrive Bramble Nature Connection Experiences & Spornivale Psilocybin Journeys

I would like a single sheet flyer (8.3" x 3.9") that advertises 2 outdoor experiences that I offer.
Side 1: Thrive Bramble Nature Connection Experiences (Logo)
3-Day Fernridge Basin Renewal Journey (Lakes, yoga, rafting Pics)
Mira SUP yoga
IMG_3136.jpg
Lost Lake with hood.jpg
At Bottom : Working with Sporanivale to bring you incredible psilocybin Journeys (w/Logo)
Side 2: North Umpqua Rafting (Crater Lake)
Rosalind Clear Falls
Crater Lake Shadows
20170606_.jppg
IMG_2779 (Remove "PDX" on raft)
Bottom: (555) 284-0937
or discover more at:
ThriveBramble.com (Nature Connection Journeys)
Sporanivale.com (Psilocybin Facilitation & Journeys)
Also include small staff pictures somewhere
Text: Find out more at sporanivale.com or ThriveBramble.com
Psilocybin / spiritual retreat

```html
<!DOCTYPE html>
<html lang="en">
<head>
<meta charset="utf-8">
<title>Thrive Bramble Flyer – Front and Back</title>
<link rel="stylesheet" href="https://fonts.googleapis.com/css2?family=Poppins:wght@300;400;600;700&family=Josefin+Sans:wght@300;400&family=Great+Vibes&family=Playfair+Display:wght@400&display=swap">
<style>
  :root {
    --navy: #1f1736;
    --navy-deep: #17112a;
    --orange: #f05a14;
    --orange-light: #ff7d22;
    --white: #ffffff;
    --page: #f1f1f1;
    --sky-top: #3f9be0;
    --sky-bottom: #dbeef9;
  }
  * { box-sizing: border-box; margin: 0; padding: 0; }
  html, body {
    width: 1200px; height: 2597px; overflow: hidden;
    background: var(--page);
  }
  .sheet {
    position: absolute; top: 724px;
    width: 388px; height: 825px;
    transform: scale(1.392); transform-origin: top left;
    background: var(--white);
    overflow: hidden;
    box-shadow: 0 2px 10px rgba(0,0,0,.18);
    font-family: "Poppins", sans-serif;
  }
  .sheet--front { left: 30px; }
  .sheet--back { left: 630px; }
  .abs { position: absolute; }
  .photo { position: absolute; }

  /* Front */
  .hero-sky {
    left: 0; top: 0; width: 388px; height: 543px;
    background: linear-gradient(180deg, var(--sky-top) 0%, #8cc6ee 35%, var(--sky-bottom) 55%, #e8eef2 60%, #1f3a24 64%, #203c62 72%, #2a5d94 88%, #1c3f6b 100%);
  }
  .brand {
    display: flex; align-items: center; gap: 18px;
  }
  .brand__dot {
    width: 58px; height: 58px; border-radius: 50%;
    background: var(--navy);
  }
  .brand__name {
    font-family: "Josefin Sans", sans-serif; font-weight: 300;
    text-transform: uppercase; letter-spacing: 3px;
    color: var(--navy);
  }
  .front-brand { left: 73px; top: 31px; }
  .front-brand .brand__name { font-size: 27px; }
  .title-num {
    left: 52px; top: 112px;
    font-family: "Playfair Display", serif; font-size: 50px; color: var(--navy-deep);
  }
  .title-script {
    left: 96px; top: 100px;
    font-family: "Great Vibes", cursive; font-size: 72px; color: var(--navy-deep);
    line-height: 1;
  }
  .title-place {
    left: 167px; top: 104px;
    font-weight: 700; font-size: 27px; color: var(--navy-deep); letter-spacing: .5px;
  }
  .title-main {
    left: 103px; top: 140px;
    font-weight: 700; font-size: 66px; color: var(--orange); line-height: 1.1;
  }
  .title-sub {
    left: 0; width: 388px; top: 218px; text-align: center;
    font-family: "Josefin Sans", sans-serif; font-weight: 400;
    font-size: 45px; line-height: 43px; color: var(--navy-deep);
  }
  .caption-band {
    left: 0; top: 503px; width: 388px; height: 40px;
    background: rgba(31,23,54,.82);
    color: var(--orange); font-size: 19px; font-weight: 300;
    display: flex; align-items: center; justify-content: center;
  }
  .thumb { top: 548px; height: 104px; }
  .thumb--yoga { left: 0; width: 191px; background: linear-gradient(160deg, #5d6a43, #7a8f7a 55%, #2e5c6e); }
  .thumb--lost-lake { left: 197px; width: 191px; background: linear-gradient(180deg, #1e6fd0, #7fb2e3 35%, #2f6b2a 60%, #3f6a55); }
  .partner {
    left: 43px; top: 677px; width: 200px;
    font-size: 13.4px; line-height: 16px; color: var(--navy-deep);
  }
  .partner-mark {
    left: 247px; top: 682px; width: 70px; height: 70px; border-radius: 50%;
    background: var(--navy);
  }
  .partner-name {
    left: 227px; top: 754px; width: 110px; text-align: center;
    font-size: 1px; color: transparent;
  }

  /* Footer */
  .footer { left: 0; top: 755px; width: 388px; height: 70px; display: flex; }
  .footer__phone {
    width: 178px; background: var(--navy); color: var(--white);
    display: flex; align-items: center; justify-content: center; gap: 6px;
    font-size: 14px; font-weight: 300;
  }
  .footer__cta {
    flex: 1; background: linear-gradient(90deg, var(--orange), var(--orange-light));
    color: var(--white); padding: 14px 0 0 14px;
  }
  .footer__label { font-size: 16px; font-weight: 400; line-height: 18px; }
  .footer__url { display: flex; align-items: center; gap: 5px; font-size: 13.5px; margin-top: 6px; }

  /* Back */
  .rafting-photo {
    left: 0; top: 0; width: 388px; height: 397px;
    background: linear-gradient(160deg, #1d2414 0%, #3b4a27 30%, #c9d2d6 45%, #e0a020 65%, #f3c21a 80%, #3a2a1f 100%);
  }
  .headline-block {
    left: 0; top: 397px; width: 388px; height: 148px;
    background: var(--navy-deep); text-align: center; color: var(--white);
  }
  .headline-block__line1 { font-weight: 700; font-size: 35px; line-height: 1; padding-top: 20px; letter-spacing: .5px; }
  .headline-block__line2 { font-weight: 700; font-size: 43px; line-height: 1.05; }
  .headline-block__sub { color: var(--orange); font-weight: 300; font-size: 18px; margin-top: 3px; }
  .thumb-back { top: 550px; height: 108px; }
  .thumb--crater { left: 0; width: 191px; background: linear-gradient(180deg, #6f7d9a, #3d4f78 45%, #1d2a4c); }
  .thumb--falls { left: 197px; width: 191px; background: linear-gradient(120deg, #2b3a22, #c9d3d6 45%, #4b5d3a 80%); }
  .back-brand { left: 60px; top: 680px; }
  .back-brand .brand__name { font-size: 28px; }
</style>
</head>
<body>

<section class="sheet sheet--front" aria-label="Flyer front">
  <div class="photo hero-sky" role="img" aria-label="Blue sky over an evergreen-lined mountain lake with a snowy peak"></div>
  <div class="abs brand front-brand"><span class="brand__dot"></span><span class="brand__name">Thrive Bramble</span></div>
  <div class="abs title-num">3</div>
  <div class="abs title-script">Day</div>
  <div class="abs title-place">FERNRIDGE</div>
  <div class="abs title-main">BASIN</div>
  <div class="abs title-sub">RENEWAL<br>JOURNEY</div>
  <div class="abs caption-band">LAKES, YOGA, RAFTING PICS</div>
  <div class="photo thumb thumb--yoga" role="img" aria-label="Paddleboard yoga pose on a forest river"></div>
  <div class="photo thumb thumb--lost-lake" role="img" aria-label="Green forest lake under a blue sky"></div>
  <p class="abs partner">Working with Sporanivale to bring you incredible psilocybin Journeys</p>
  <div class="abs partner-mark" aria-label="Sporanivale"></div>
  <div class="abs footer">
    <div class="footer__phone">
      <svg width="12" height="12" viewBox="0 0 24 24" fill="none" stroke="#fff" stroke-width="2"><path d="M5 3h4l2 5-3 2a12 12 0 0 0 6 6l2-3 5 2v4a2 2 0 0 1-2 2A18 18 0 0 1 3 5a2 2 0 0 1 2-2z"/></svg>
      (555) 284-0937
    </div>
    <div class="footer__cta">
      <div class="footer__label">DISCOVER MORE AT</div>
      <div class="footer__url">
        <svg width="13" height="13" viewBox="0 0 24 24" fill="none" stroke="#fff" stroke-width="2"><circle cx="12" cy="12" r="10"/><path d="M2 12h20M12 2a15 15 0 0 1 0 20M12 2a15 15 0 0 0 0 20"/></svg>
        ThriveBramble.com
      </div>
    </div>
  </div>
</section>

<section class="sheet sheet--back" aria-label="Flyer back">
  <div class="photo rafting-photo" role="img" aria-label="Rafters in yellow helmets paddling through whitewater"></div>
  <div class="abs headline-block">
    <div class="headline-block__line1">NORTH UMPQUA</div>
    <div class="headline-block__line2">RAFTING</div>
    <div class="headline-block__sub">(CRATER LAKE)</div>
  </div>
  <div class="photo thumb-back thumb--crater" role="img" aria-label="Silhouettes above a deep blue crater lake"></div>
  <div class="photo thumb-back thumb--falls" role="img" aria-label="Hiker beside a forest waterfall"></div>
  <div class="abs brand back-brand"><span class="brand__dot"></span><span class="brand__name">Thrive Bramble</span></div>
  <div class="abs footer">
    <div class="footer__phone">
      <svg width="12" height="12" viewBox="0 0 24 24" fill="none" stroke="#fff" stroke-width="2"><path d="M5 3h4l2 5-3 2a12 12 0 0 0 6 6l2-3 5 2v4a2 2 0 0 1-2 2A18 18 0 0 1 3 5a2 2 0 0 1 2-2z"/></svg>
      (555) 284-0937
    </div>
    <div class="footer__cta">
      <div class="footer__label">DISCOVER MORE AT</div>
      <div class="footer__url">
        <svg width="13" height="13" viewBox="0 0 24 24" fill="none" stroke="#fff" stroke-width="2"><circle cx="12" cy="12" r="10"/><path d="M2 12h20M12 2a15 15 0 0 1 0 20M12 2a15 15 0 0 0 0 20"/></svg>
        Sporanivale.com
      </div>
    </div>
  </div>
</section>

</body>
</html>
```